FItness Bootcamp Flyer

We need an A4 flyer to distribute on an advertising board, and also distribute in the mail.

It should contain a photo(s) of females exercising and having fun outdoors.

It should contain the following text and if you think it could be worded better please change as I'm just looking at getting people to come along:

- KestrelMove Studio Outdoor Bootcamp
Get moving, get fit and feel great

Commencing 19th May

Get results before the winter season
6 Week Bootcamp for $49. Limited numbers!
Or casual visit $10 per session

Now is the time to:
- Lose Weight and Tone-up
- Build Strength and Endurance
- Increase Cardio Fitness
- Improve Your Energy and Vitality
- Fun Varied and Exciting Training Programs
- ALL Fitness Levels

LADIES ONLY BOOTCAMP SUBIACO
Monday 6:30-7:15am, 8:30-9:15am
Wednesday 6:30-7:!5am, 8:30-9:15am
Friday 8:30-9:15am,

Register you place now on 0428 574 812 or email: kestrelmovestudio@fernmail.net

facebook.com/KestrelMove Studio

Target Market(s)

Females 20-60yrs

Industry/Entity Type

Advertising

Requirements
Nice to have
• - We like the words and style of the Harbourline Open Air Training flyer attached
- Also the Vanta Group brochure
- I like the colour Blue, Green, Pink. They don't all have to be used but at least one would be nice thank you

```html
<!DOCTYPE html>
<html lang="en">
<head>
<meta charset="utf-8">
<title>KestrelMove Studio Outdoor Bootcamp</title>
<link href="https://fonts.googleapis.com/css2?family=Ubuntu:wght@400;500;700&display=swap" rel="stylesheet">
<style>
  :root {
    --green-light: #8dc63f;
    --green-mid: #5cb845;
    --green-dark: #2e8b3a;
    --green-deep: #1f7a32;
    --white: #ffffff;
    --ring: #c9cccf;
    --photo-sand: #b9ad86;
    --photo-sky: #d9d8cf;
  }
  html, body { margin: 0; padding: 0; overflow: hidden; }
  body { width: 933px; height: 1200px; font-family: "Ubuntu", sans-serif; }
  .flyer { position: relative; width: 933px; height: 1200px; overflow: hidden; background: var(--green-light); }
  .backdrop { position: absolute; inset: 0; }
  .hero-photo {
    position: absolute; left: 140px; top: 0; width: 793px; height: 660px;
    background: linear-gradient(180deg, var(--photo-sky) 0%, #c8c3ad 35%, var(--photo-sand) 60%, #8f8262 100%);
  }
  .overlay { position: absolute; inset: 0; }
  .brand {
    position: absolute; left: 172px; top: 40px; margin: 0;
    font-weight: 700; font-size: 50px; line-height: 56px; letter-spacing: 4px;
    color: var(--green-mid); text-transform: uppercase;
  }
  .tagline {
    position: absolute; left: 175px; top: 196px; margin: 0;
    font-weight: 500; font-size: 29px; line-height: 37px; color: var(--white);
  }
  .circle {
    position: absolute; border-radius: 50%; box-sizing: border-box;
    border: 8px solid var(--ring); box-shadow: inset 0 0 0 4px var(--white), 0 3px 8px rgba(0,0,0,.25);
  }
  .circle-class { left: 60px; top: 440px; width: 290px; height: 290px; background: linear-gradient(135deg, #e8e4e0, #b9c6d2 60%, #8a7a6c); }
  .circle-rower { left: 155px; top: 645px; width: 258px; height: 258px; background: linear-gradient(160deg, #dcdcdc, #b8b0a6 50%, #e08a3a 85%); }
  .circle-weights { left: 45px; top: 800px; width: 255px; height: 255px; background: linear-gradient(160deg, #d6dbe0, #c7b8a8 45%, #3f6fb0 85%); }
  .offer { position: absolute; right: 33px; top: 625px; text-align: right; color: var(--green-dark); font-weight: 700; }
  .offer-date { margin: 0 0 18px; font-size: 44px; line-height: 54px; color: var(--green-light); }
  .offer-line { margin: 0; font-size: 19px; line-height: 33px; }
  .offer-line .big { font-size: 24px; }
  .offer-lead { margin: 4px 0 2px; font-size: 24px; line-height: 34px; color: var(--green-light); }
  .benefits { list-style: none; margin: 0; padding: 0; font-size: 21px; line-height: 31.5px; }
  .footer-band { position: absolute; left: 0; top: 1040px; width: 933px; height: 160px; }
  .schedule { position: absolute; left: 110px; top: 1065px; width: 400px; margin: 0; text-align: center; color: var(--white); font-weight: 700; font-size: 19px; line-height: 25px; }
  .schedule-title { font-size: 20px; }
  .register { position: absolute; left: 560px; top: 1063px; width: 360px; margin: 0; text-align: center; color: var(--white); font-weight: 700; font-size: 17px; line-height: 25px; }
</style>
</head>
<body>
<main class="flyer">
  <svg class="backdrop" width="933" height="1200" viewBox="0 0 933 1200" aria-hidden="true">
    <rect width="933" height="1200" fill="var(--green-light)"/>
    <path d="M0 0 H150 C120 200 110 380 140 520 C100 650 90 850 95 1040 H0 Z" fill="var(--green-mid)"/>
    <path d="M30 0 H120 C95 200 90 380 115 520 C80 650 70 850 75 1040 H30 Z" fill="#4fae41"/>
    <path d="M60 0 H95 C75 200 70 380 92 520 C60 650 55 850 58 1040 H60 Z" fill="var(--green-light)" opacity=".6"/>
  </svg>

  <div class="hero-photo" role="img" aria-label="Photo of a woman doing a push-up on a sandy rooftop outdoors, city buildings behind"></div>

  <svg class="overlay" width="933" height="1200" viewBox="0 0 933 1200" aria-hidden="true">
    <path d="M95 1040 L933 1040 L933 590 C800 592 650 602 520 625 C420 645 360 662 300 700 C180 780 110 900 95 1040 Z" fill="var(--white)"/>
    <rect class="footer-rule" x="95" y="1040" width="838" height="5" fill="var(--green-deep)"/>
  </svg>

  <h1 class="brand">KestrelMove<br>Studio</h1>
  <p class="tagline">KestrelMove Studio<br>Outdoor Bootcamp<br>Get moving,<br>get fit and<br>feel great</p>

  <div class="circle circle-class" role="img" aria-label="Photo of women smiling in a group fitness class"></div>
  <div class="circle circle-rower" role="img" aria-label="Photo of a woman training on a rowing machine"></div>
  <div class="circle circle-weights" role="img" aria-label="Photo of a class lifting hand weights on mats"></div>

  <section class="offer">
    <p class="offer-date">Commencing 19th May</p>
    <p class="offer-line">Get results before the winter season</p>
    <p class="offer-line"><span class="big">6</span> Week Bootcamp for <span class="big">$49</span>. Limited numbers!</p>
    <p class="offer-line">Or casual visit <span class="big">$10</span> per session</p>
    <p class="offer-lead">Now is the time to:</p>
    <ul class="benefits">
      <li>- Lose Weight and Tone-up</li>
      <li>- Build Strength and Endurance</li>
      <li>- Increase Cardio Fitness</li>
      <li>- Improve Your Energy and Vitality</li>
      <li>- Fun Varied and Exciting Training Programs</li>
      <li>- ALL Fitness Levels</li>
    </ul>
  </section>

  <p class="schedule"><span class="schedule-title">LADIES ONLY BOOTCAMP SUBIACO</span><br>Monday 6:30-7:15am, 8:30-9:15am<br>Wednesday 6:30-7:15am, 8:30-9:15am<br>Friday 8:30-9:15am,</p>
  <p class="register">Register you place now on<br>0428 574 812 or<br>email: kestrelmovestudio@fernmail.net<br>facebook.com/KestrelMove Studio</p>
</main>
</body>
</html>
```